Business Card Design Project

We need a Business Card for an Mechanical Engineering firm in Singapore. The design should be Modern & Technical looking, yet eye catching.

Our company deals in Cutting Tools & Machine Accessories for the Manufacturing Industries such as Oil & Gas, Aero Space, etc... For more information on our Company, you can either email me or view our website www.valtrion.com.sg.

We are trying to revamp our image to give our consumers a fresh new perspective to our company, so we welcome all ideas.

Industry/Entity Type

Business

Requirements
Must have
• Must incorporate New Company Logo into the card as shown in Uploaded file.

```html
<!DOCTYPE html>
<html lang="en">
<head>
<meta charset="utf-8">
<title>Valtrion Tools – Business Card</title>
<link href="https://fonts.googleapis.com/css2?family=Tenor+Sans&display=swap" rel="stylesheet">
<style>
  :root {
    --page-bg: #3a3a3a;
    --card-bg: #141414;
    --card-edge: #1c1c1c;
    --pattern-tone: #222222;
    --ink: #e9e9e9;
    --ink-soft: #d4d4d4;
  }
  * { margin: 0; padding: 0; box-sizing: border-box; }
  html, body {
    width: 1067px;
    height: 1200px;
    overflow: hidden;
    background: var(--page-bg);
    font-family: "Tenor Sans", sans-serif;
  }
  .sheet {
    width: 1067px;
    height: 1200px;
    display: flex;
    flex-direction: column;
    align-items: center;
    justify-content: center;
    gap: 76px;
  }
  .card {
    position: relative;
    width: 860px;
    height: 491px;
    background: var(--card-bg);
    overflow: hidden;
  }
  .card-pattern {
    position: absolute;
    inset: 0;
    background:
      radial-gradient(circle at 30% 60%, var(--pattern-tone) 0%, transparent 38%),
      radial-gradient(circle at 80% 30%, var(--pattern-tone) 0%, transparent 30%),
      linear-gradient(135deg, var(--card-edge), var(--card-bg));
  }
  .card-content { position: absolute; inset: 0; }

  /* Front */
  .front .card-content {
    display: flex;
    flex-direction: column;
    align-items: center;
    justify-content: center;
  }
  .brand-name {
    color: var(--ink);
    font-size: 58px;
    letter-spacing: 2px;
    text-transform: uppercase;
    line-height: 1;
  }
  .front .website {
    margin-top: 44px;
    color: var(--ink);
    font-size: 20px;
    letter-spacing: 4px;
  }

  /* Back */
  .back .card-content {
    padding: 56px 64px 0 0;
    display: flex;
    flex-direction: column;
    align-items: flex-end;
    text-align: right;
  }
  .back .brand-name { font-size: 44px; }
  .company-name {
    margin-top: 40px;
    color: var(--ink);
    font-size: 26px;
    letter-spacing: 1px;
  }
  .contact-block {
    margin-top: 12px;
    color: var(--ink-soft);
    font-size: 15px;
    line-height: 1.45;
    letter-spacing: 0.5px;
  }
  .contact-block p + p.gap { margin-top: 22px; }
</style>
</head>
<body>
<main class="sheet">
  <section class="card front">
    <div class="card-pattern" role="img" aria-label="Faint background pattern of interlocking gear shapes"></div>
    <div class="card-content">
      <h1 class="brand-name">Valtrion Tools</h1>
      <p class="website">www.valtrion.com.sg</p>
    </div>
  </section>

  <section class="card back">
    <div class="card-pattern" role="img" aria-label="Faint background pattern of interlocking gear shapes"></div>
    <div class="card-content">
      <h2 class="brand-name">Valtrion Tools</h2>
      <p class="company-name">Valtrion Tools Pte Ltd</p>
      <div class="contact-block">
        <p>27 Kestrel Way #03-08, Northgate Works Centre</p>
        <p>Singapore 609417</p>
        <p class="gap">t: 65-61230457 / f: 65-61230458</p>
        <p>e: hello@valtrion.com.sg / w: www.valtrion.com.sg</p>
      </div>
    </div>
  </section>
</main>
</body>
</html>
```